Security Company Needs a Website *

We need a website that gives our clients information about the services we provide, methods of contacting us and landing page to advertise on social media sites.

We need five landing pages titled Home, About Us, Services, Contact Us and a Landing Page that can be linked to Chatterloop advertising.

About Us - Should have a section for Core Values & Ethics, Our Vision, Our Mission and Partners.

Services - This page should show the different categories which include CCTV, Security Alarms, Access Control and Fire Protection.

CCTV Service Description:
Closed circuit television (CCTV) has long been implemented by businesses as a surveillance tool in areas that need monitoring. With digital CCTV cameras, multiple video cameras transmit signals through a set of monitors. The cameras provide thorough surveillance of the area.

With vast technological improvements over the last ten years, businesses with CCTV systems can use unique IP cameras and video analytics to monitor traffic flows, people-count, implement facial and number plate recognition. Useful information about customer behaviour and demographics can be discovered too. CCTV helps prevent crime in many industries and can assist with the improvement of industrial processes, safety on transport systems and traffic monitoring.

Security Alarms Service Description:
Alarms systems are electronic devices programmed to alert people to specific dangers and detect intrusions, fire or theft. Security alarms, systems and access control monitoring combine to create an integrated surveillance solution, tailored to your business’ unique requirements. Our surveillance and alarm monitoring services are ideal for perimeter protection from unwanted intruders or potential dangers.

Access Control Services:
An access control system allows for the free flow of authorised personnel while denying entry to unwanted visitors. With walk-in thieves and trespassers shut out, you dramatically reduce your exposure to crime while increasing the security of your employees, visitors, information and assets.

* Control when and who is entering your premises
* Protect employees, assets and information
* Secure an area or sector
* Observe movement
* Integrate with other security systems

Our range of access control systems can be seamlessly linked to other systems in our portfolio. These include Fire Detection Systems, Intruder Alarms, CCTV, and Building Management. A common request involves the need for a CCTV camera to pan around and focus on a door that has been highlighted as a security risk by the access control system.

Fire Protection Service:
To Be Advised

The above copy-writing will also have to be changed.

Contact Us - This form needs to be simple and straightforward to gather the prospects information and we would like to have a call to action on this page. The Contact Us page should also have a wayfindr charts location of our office address.

We would also like to have a link to our chatterloop page on the website.

Target Market(s)

Commercial businesses, building construction developers and property managers.

Industry/Entity Type

Security

Number of Pages Required

5+ page

Font styles to use
Sans Serif

Colors

Designer to choose colors to be used in the design.

Requirements
Must have
• We need to have the same look and feel as well as website features as the following website:
• https://www.kelvaguard.example.au/business-security/
• The website must be easy to use and easy to edit as well.

```html
<!DOCTYPE html>
<html lang="en">
<head>
<meta charset="utf-8">
<title>Security Solutions — Our Services</title>
<link href="https://fonts.googleapis.com/css2?family=Poppins:wght@300;400;500;600;700&display=swap" rel="stylesheet">
<style>
  :root{
    --navy:#1e1552;
    --blue:#0a67b0;
    --blue-active:#2d3a8f;
    --link:#15397a;
    --phone:#1b4f91;
    --page-bg:#f3f3f3;
    --muted:#8a8a8a;
    --body:#444;
    --footer:#0b0b0b;
    --footer-line:#3a3a3a;
    --footer-muted:#8e8e8e;
    --accent-link:#2f7fe0;
  }
  *{box-sizing:border-box;margin:0;padding:0}
  html,body{width:1200px;height:1170px;overflow:hidden}
  body{font-family:'Poppins',sans-serif;background:#fff;color:var(--body);position:relative}
  .wrap{position:absolute;left:154px;width:892px}

  /* header */
  .site-header{position:absolute;top:0;left:0;width:1200px;height:65px;background:#fff}
  .brand{position:absolute;left:154px;top:7px;display:flex;align-items:center}
  .brand-mark{width:51px;height:51px;border-radius:50%;background:var(--blue-active);display:flex;align-items:center;justify-content:center;color:#fff;font-size:12px;font-weight:400}
  .brand-text{margin-left:12px;color:var(--navy);line-height:1}
  .brand-name{font-size:18px;font-weight:400;letter-spacing:-.2px}
  .brand-tag{font-size:9.5px;font-weight:400;margin-top:3px;padding-left:20px}
  .call{position:absolute;right:154px;top:11px;color:var(--phone);font-weight:600;font-size:16px;line-height:22px}

  /* nav */
  .main-nav{position:absolute;top:65px;left:0;width:1200px;height:37px;background:var(--blue)}
  .main-nav ul{list-style:none;display:flex;position:absolute;left:154px;top:0;height:37px;border-left:1px solid rgba(255,255,255,.12)}
  .main-nav li{color:#fff;font-size:13.5px;font-weight:400;height:37px;line-height:37px;border-right:1px solid rgba(255,255,255,.12)}
  .main-nav li.home{width:79px;text-align:center}
  .main-nav li.about{width:101px;text-align:center;background:var(--blue-active)}
  .main-nav li.services{width:98px;text-align:center}
  .main-nav li.contact{width:120px;text-align:center}
  .search{position:absolute;left:838px;top:0;width:208px;height:37px;border-left:1px solid rgba(255,255,255,.12);border-right:1px solid rgba(255,255,255,.12);color:rgba(255,255,255,.6);font-size:11px;line-height:37px;padding-left:16px}
  .search svg{position:absolute;right:14px;top:12px}

  /* services */
  .services{position:absolute;top:102px;left:0;width:1200px;height:699px;background:var(--page-bg)}
  .section-title{position:absolute;left:0;width:1200px;top:20px;text-align:center;color:var(--navy);font-size:23px;font-weight:600}
  .section-rule{position:absolute;left:579px;top:53px;width:42px;height:1px;background:var(--navy)}
  .lead{position:absolute;left:0;width:1200px;top:71px;text-align:center;font-size:13px;font-weight:300;color:#333}
  .photo{position:absolute}
  .photo.cctv{left:157px;top:117px;width:416px;height:254px;background:linear-gradient(135deg,#6d98c6 0%,#9cc0e0 45%,#5e8fb8 75%,#3c6a3f 100%)}
  .photo.alarm{left:629px;top:372px;width:416px;height:255px;background:radial-gradient(circle at 60% 50%,#e03a36 0 18%,#e4e4e4 19%,#d0d0d0 100%)}
  .service-title{position:absolute;color:var(--navy);font-size:23px;font-weight:600}
  .service-text{position:absolute;font-size:13.4px;font-weight:300;color:var(--muted);line-height:20.8px}
  .cctv-title{left:628px;top:142px}
  .cctv-text{left:628px;top:184px;width:420px}
  .alarm-title{left:157px;width:416px;text-align:right;top:404px}
  .alarm-text{left:155px;width:418px;text-align:right;top:445px}
  .more{position:absolute;display:flex;align-items:center;gap:14px;color:var(--link);font-size:13.5px;font-weight:500}
  .read-more{left:630px;top:299px}
  .load-more{left:565px;top:652px}

  /* footer */
  .site-footer{position:absolute;top:801px;left:0;width:1200px;height:369px;background:linear-gradient(120deg,#050505 0%,#1a1a1c 38%,#0a0a0a 39%,#111 70%,#060606 100%);color:#fff}
  .footer-title{position:absolute;left:153px;top:23px;font-size:23px;font-weight:600}
  .footer-rule{position:absolute;left:155px;top:52px;width:48px;height:1px;background:#fff}
  .field{position:absolute;border:1px solid #6a6a6a;color:#777;font-size:11.5px;font-weight:300;padding-left:10px;line-height:25px}
  .f-name{left:152px;top:82px;width:218px;height:27px}
  .f-email{left:390px;top:82px;width:217px;height:27px}
  .f-phone{left:152px;top:127px;width:218px;height:27px}
  .f-company{left:390px;top:127px;width:217px;height:27px}
  .f-message{left:152px;top:173px;width:455px;height:104px;padding-top:4px}
  .send{position:absolute;left:154px;top:286px;display:flex;gap:14px;align-items:center;font-size:13.5px;font-weight:500;color:#fff}
  .col-title{position:absolute;font-size:17px;font-weight:500}
  .touch-title{left:647px;top:89px}
  .links-title{left:902px;top:89px}
  .touch-item{position:absolute;left:647px;font-size:12px}
  .touch-item .label{display:flex;align-items:center;gap:10px}
  .touch-item .value{padding-left:25px;margin-top:7px;color:var(--footer-muted);font-weight:300}
  .ti-office{top:114px}
  .ti-office .value{margin-top:13px}
  .ti-email{top:173px}
  .ti-phone{top:226px}
  .quick{position:absolute;left:904px;top:117px;list-style:none;font-size:11.5px;color:var(--footer-muted);font-weight:300}
  .quick li{height:26.4px}
  .footer-bottom{position:absolute;left:153px;top:332px;width:893px;border-top:1px solid var(--footer-line)}
  .copyright{position:absolute;left:0;top:11px;font-size:11.5px;font-weight:300}
  .copyright span{color:var(--accent-link)}
  .social{position:absolute;right:0;top:12px;display:flex;gap:14px;list-style:none;font-size:10.5px;font-weight:500}
</style>
</head>
<body>

<header class="site-header">
  <div class="brand">
    <div class="brand-mark">Norvane</div>
    <div class="brand-text">
      <div class="brand-name">SECURITY SOLUTIONS</div>
      <div class="brand-tag">EXCEEDING EXPECTATIONS</div>
    </div>
  </div>
  <div class="call">Call Us Now<br>(080) 41720 38846</div>
</header>

<nav class="main-nav">
  <ul>
    <li class="home">Home</li>
    <li class="about">About Us</li>
    <li class="services">Services</li>
    <li class="contact">Contact&nbsp; Us</li>
  </ul>
  <div class="search">Search
    <svg width="13" height="13" viewBox="0 0 13 13" fill="none" stroke="rgba(255,255,255,.7)" stroke-width="1.8"><circle cx="5.5" cy="5.5" r="4.3"/><line x1="8.7" y1="8.7" x2="12" y2="12"/></svg>
  </div>
</nav>

<main class="services">
  <h1 class="section-title">Our Services</h1>
  <div class="section-rule"></div>
  <p class="lead">Ut enim ad minim veniam, quis nostrud exercitation ullamco laboris nisi ut aliquip ex ea commodo consequat.</p>

  <div class="photo cctv" role="img" aria-label="Dome CCTV camera mounted on a pole in front of a glass office building"></div>
  <h2 class="service-title cctv-title">CCTV</h2>
  <p class="service-text cctv-text">Closed circuit television (CCTV) has long been implemented by businesses as a surveillance tool in areas that need monitoring. With digital CCTV cameras, multiple video cameras transmit signals through a set of monitors. The cameras provide thorough surveillance of the area.</p>
  <div class="more read-more">
    <svg width="14" height="8" viewBox="0 0 14 8" fill="none" stroke="currentColor" stroke-width="1.4"><line x1="0" y1="4" x2="12.5" y2="4"/><polyline points="9.5,1 12.8,4 9.5,7"/></svg>
    Read More
  </div>

  <h2 class="service-title alarm-title">Security Alarms</h2>
  <p class="service-text alarm-text">Alarms systems are electronic devices programmed to alert people to specific dangers and detect intrusions, fire or theft. Security alarms, systems and access control monitoring combine to create an integrated surveillance solution, tailored to your business’ unique requirements. Our surveillance and alarm monitoring services are ideal for perimeter protection from unwanted intruders or potential dangers.</p>
  <div class="photo alarm" role="img" aria-label="Red pull-down fire alarm box on a white wall"></div>

  <div class="more load-more">
    <svg width="14" height="8" viewBox="0 0 14 8" fill="none" stroke="currentColor" stroke-width="1.4"><line x1="0" y1="4" x2="12.5" y2="4"/><polyline points="9.5,1 12.8,4 9.5,7"/></svg>
    Load More
  </div>
</main>

<footer class="site-footer">
  <h2 class="footer-title">Contact Us</h2>
  <div class="footer-rule"></div>

  <div class="field f-name">Name</div>
  <div class="field f-email">Email</div>
  <div class="field f-phone">Phone</div>
  <div class="field f-company">Company</div>
  <div class="field f-message">Message</div>
  <div class="send">
    <svg width="14" height="8" viewBox="0 0 14 8" fill="none" stroke="#fff" stroke-width="1.4"><line x1="0" y1="4" x2="12.5" y2="4"/><polyline points="9.5,1 12.8,4 9.5,7"/></svg>
    Send Now
  </div>

  <h3 class="col-title touch-title">Get in Touch</h3>
  <div class="touch-item ti-office">
    <div class="label"><svg width="14" height="12" viewBox="0 0 14 12" fill="#fff"><polygon points="7,0 14,6 12,6 12,12 8.5,12 8.5,8 5.5,8 5.5,12 2,12 2,6 0,6"/></svg>Office Address</div>
    <div class="value">48 Harrow Lane, Bramwick, UK</div>
  </div>
  <div class="touch-item ti-email">
    <div class="label"><svg width="15" height="11" viewBox="0 0 15 11" fill="none" stroke="#fff" stroke-width="1.2"><rect x="0.6" y="0.6" width="13.8" height="9.8" rx="1"/><polyline points="0.8,1 7.5,6 14.2,1"/></svg>Email</div>
    <div class="value">hello@norvane.example</div>
  </div>
  <div class="touch-item ti-phone">
    <div class="label"><svg width="14" height="14" viewBox="0 0 14 14" fill="#fff"><path d="M3 0.5l2.2 3-1.3 1.6c.8 1.8 2.2 3.2 4 4l1.6-1.3 3 2.2-1.3 2.7C6 12.5 1.5 8 .5 1.8z"/></svg>Phone</div>
    <div class="value">(080) 41720 59013</div>
  </div>

  <h3 class="col-title links-title">Quick links</h3>
  <ul class="quick">
    <li>Home</li>
    <li>About Us</li>
    <li>Services</li>
    <li>FAQ</li>
    <li>Customer Support</li>
    <li>Privacy Polacy</li>
  </ul>

  <div class="footer-bottom">
    <p class="copyright">© Copyright 2018 - <span>Security Soutions</span> - All right reserved.</p>
    <ul class="social">
      <li>Chatterloop</li>
      <li>Flitter</li>
      <li>Workweave</li>
      <li>Orbitly</li>
    </ul>
  </div>
</footer>

</body>
</html>
```